Flyer-Design für Eröffnung des Salons Belle Rivane gesucht
Zielgruppe
Es soll sehr gut mit meinem Website harmonisieren.
www.belle-rivane.ch
Aufgabenstellung
Ich eröffne einen Kosmetiksalon und wünsche mir einen schönen Flyer zur Ankündigung der Eröffnung. Bitte in A5 im Hochformat erstellen.
Der Flyer soll auch einen Gutschein für eine Gesichtsbehandlung im Wert von 30 Chf enthalten (nach Möglichkeit rechts oben auf dem Flyer, in einer gut sichtbaren Farbe).
Auf den Seiten des Flyers wünsche ich einfache Abschlüsse mit sanften Farben oder in Schwarz-weissem Grauton Blumendesign.
Der ganze Flyer soll eher simple wirken und dennoch ein Blickfang sein,darf nicht kitschig auffallen sondern soll Klasse und Edel wirken.
Mittig soll Platz sein fur vier Linien Text,d.h ein noch nicht ganz definiertes Angebot für drei Arten von Gesichtsbehandlungen und eiem speziellen Angebot. Im moment können noch Fantasietexte als Platzhalter dienen.

```html
<!DOCTYPE html>
<html lang="de">
<head>
<meta charset="utf-8">
<title>Belle Rivane – Neueröffnung Flyer</title>
<link href="https://fonts.googleapis.com/css2?family=Jost:wght@400;500;600;700&display=swap" rel="stylesheet">
<style>
  :root {
    --sky: #7cc8de;
    --sky-pale: #e6f3f6;
    --taupe: #a0928b;
    --taupe-dark: #8e807a;
    --paper: #ffffff;
    --canvas: #ffffff;
    --skin-light: #f6ebe3;
    --skin: #ecd3c3;
    --petal: #f3d2a6;
  }
  * { box-sizing: border-box; margin: 0; padding: 0; }
  html, body { width: 1200px; height: 848px; overflow: hidden; background: var(--canvas); }
  body { position: relative; font-family: "Jost", sans-serif; color: var(--taupe); }

  .flyer {
    position: absolute; top: 117px; width: 423px; height: 600px;
    background: var(--paper);
    box-shadow: 0 0 3px rgba(0,0,0,0.25);
    overflow: hidden;
  }
  .flyer--front { left: 138px; }
  .flyer--back { left: 632px; }

  /* Front */
  .hero-photo {
    position: absolute; left: 0; top: 0; width: 423px; height: 501px;
    background:
      radial-gradient(ellipse 45% 55% at 60% 38%, var(--skin) 0%, rgba(236,211,195,0.6) 55%, rgba(246,235,227,0) 100%),
      radial-gradient(ellipse 35% 40% at 25% 55%, var(--petal) 0%, rgba(243,210,166,0) 100%),
      linear-gradient(180deg, var(--skin-light) 0%, var(--skin-light) 70%, #ffffff 100%);
  }
  .opening-band {
    position: absolute; left: 0; top: 367px; width: 342px; height: 44px;
    background: var(--sky);
    box-shadow: 2px 2px 3px rgba(0,0,0,0.2);
    color: #fff; font-weight: 600; font-size: 31px; letter-spacing: 2.5px;
    line-height: 44px; padding-left: 33px;
  }
  .brand-name {
    position: absolute; font-weight: 400; font-size: 46px; letter-spacing: 1px;
    color: var(--taupe); white-space: nowrap;
  }
  .flyer--front .brand-name { left: 22px; top: 470px; }
  .flyer--back .brand-name { left: 46px; top: 470px; }
  .web-address {
    position: absolute; top: 554px; font-size: 12px; letter-spacing: 2.4px; color: var(--taupe);
  }
  .flyer--front .web-address { left: 54px; }
  .flyer--back .web-address { left: 84px; }
  .partner-brand {
    position: absolute; left: 294px; top: 550px; text-align: right;
    color: var(--taupe-dark); font-size: 13px; letter-spacing: 1px; line-height: 1;
  }
  .partner-brand small { display: block; font-size: 6px; letter-spacing: 0.5px; margin-top: 2px; }

  /* Back */
  .treatments { position: absolute; left: 14px; top: 12px; width: 394px; }
  .treatment { margin-bottom: 10px; }
  .treatment h2 {
    color: var(--sky); font-weight: 600; font-size: 15.5px; letter-spacing: 1px; line-height: 18px;
  }
  .treatment p {
    font-size: 9.4px; line-height: 13px; text-transform: uppercase; text-align: justify;
    color: var(--taupe);
  }
  .treatment .duration { float: right; }
  .treatment .duration b { font-weight: 600; }
  .treatment--thalasso .duration { display: block; float: none; text-align: right; }

  .flower-deco {
    position: absolute; left: 256px; top: 243px; width: 180px; height: 176px;
    background: var(--sky-pale);
    border-radius: 20% 45% 50% 45% / 15% 40% 55% 55%;
  }
  .voucher-value {
    position: absolute; left: 16px; top: 262px; font-size: 37px; font-weight: 700;
    letter-spacing: 1.5px; color: var(--taupe-dark);
  }
  .voucher-band {
    position: absolute; left: 0; top: 303px; width: 166px; height: 21px;
    background: var(--sky); box-shadow: 2px 2px 3px rgba(0,0,0,0.2);
    color: #fff; font-weight: 600; font-size: 15px; letter-spacing: 1px;
    line-height: 21px; padding-left: 16px;
  }
  .voucher-line {
    position: absolute; left: 15px; width: 216px; height: 1px; background: #c9c0bb;
  }
  .contact {
    position: absolute; left: 293px; top: 295px; font-size: 10px; line-height: 13.2px;
    letter-spacing: 0.3px; color: var(--taupe-dark);
  }
  .contact strong { font-weight: 600; display: block; }
</style>
</head>
<body>

<section class="flyer flyer--front">
  <div class="hero-photo" role="img" aria-label="Porträtfoto einer Frau mit gepflegter Haut und Orchideenblüten"></div>
  <div class="opening-band">NEUERÖFFNUNG</div>
  <div class="brand-name">Belle Rivane</div>
  <div class="web-address">WWW.BELLE-RIVANE.CH</div>
  <div class="partner-brand">LUMARA<small>PARIS</small></div>
</section>

<section class="flyer flyer--back">
  <div class="treatments">
    <article class="treatment">
      <h2>KURZBEHANDLUNG 99 CHF</h2>
      <p>Reinigung, Peeling, Ausreinigung, Augenbrauenkorrektur, beruhigende Maske, Abschlusspflege. <span class="duration"><b>Dauer:</b> 1.00 Stunde</span></p>
    </article>
    <article class="treatment">
      <h2>KLASSISCHE GESICHTSBEHANDLUNG 129 CHF</h2>
      <p>Reinigung,Peeling (mit oder ohne Dampf), Ausreinigung, Brauenkorrektur, Essencen-Massage, Mask, Abschlusspflege. <span class="duration"><b>Dauer:</b> 1.45 Stunde</span></p>
    </article>
    <article class="treatment treatment--thalasso">
      <h2>SOIN THALASSO 139 CHF</h2>
      <p>Feuchtigkeitsbehandlung mit vitalisierender Algenmaske Reinigung, Peeling, Ausreinigung, Essence-Massage, Algenmaske, Abschlusspflege. <span class="duration"><b>Dauer:</b> 1.50 Stunde</span></p>
    </article>
    <article class="treatment">
      <h2>ANTI-AGING BEHANDLUNG 149 CHF</h2>
      <p>Reinigung, Enzympeeling, Ausreinigung, Brauenkorrektur, Caviar Essence, Massage, Trüffelmaske, Abschlusspflege. <span class="duration"><b>Dauer:</b> 1.45 Stunde</span></p>
    </article>
  </div>

  <div class="flower-deco" role="img" aria-label="Zarte hellblaue Tulpenblüte als Dekoration"></div>

  <div class="voucher-value">30 CHF</div>
  <div class="voucher-band">GUTSCHEIN FÜR</div>
  <div class="voucher-line" style="top:358px"></div>
  <div class="voucher-line" style="top:387px"></div>
  <div class="voucher-line" style="top:416px"></div>

  <address class="contact" style="font-style:normal">
    <strong>HELENA VARGA</strong>
    <strong>KOSMETIKERIN</strong>
    LINDENWEG 9<br>
    8400 TALWIL<br>
    TELEFON: 076-555-0182
  </address>

  <div class="brand-name">Belle Rivane</div>
  <div class="web-address">WWW.BELLE-RIVANE.CH</div>
</section>

</body>
</html>
```